Medical Waste Company with Logo

Need a business card design that targets office managers in the medical community. This card will be the front line for our sales team to market our services to the community. We would like to have email, phone number, website. Please use the logo attached to create a design that we would be proud of.

Target Market(s)

Medical Clients

Industry/Entity Type

Medical Supply

Contact Information for Business Card

Please use logo attached

Colors

Designer to choose colors to be used in the design.

Requirements
Must have
• Our logo (see attached file)
Nice to have
• Maybe a pop of some sort, raised..?

```html
<!DOCTYPE html>
<html lang="en">
<head>
<meta charset="utf-8">
<title>Northpeak Clinical Disposal – Business Card</title>
<link href="https://fonts.googleapis.com/css2?family=Open+Sans:wght@400;600;700&display=swap" rel="stylesheet">
<style>
  :root {
    --backdrop: #e4e6ea;
    --card: #ffffff;
    --brand-blue: #0a52a8;
    --accent-grey: #8e8f91;
    --ink: #1c1c1c;
    --on-blue: #ffffff;
  }
  * { margin: 0; padding: 0; box-sizing: border-box; }
  html, body {
    width: 1200px; height: 977px; overflow: hidden;
    background: var(--backdrop);
    font-family: "Open Sans", Arial, sans-serif;
  }
  .business-card {
    position: absolute; left: 100px; top: 203px;
    width: 1000px; height: 571px;
    background: var(--card);
    overflow: hidden;
    box-shadow: 0 6px 22px rgba(0,0,0,0.18);
  }
  .wave-art { position: absolute; inset: 0; }
  .corner-tab {
    position: absolute; right: 0; top: 92px;
    width: 36px; height: 74px;
    background: var(--brand-blue);
  }
  .holder { position: absolute; right: 80px; top: 100px; text-align: right; }
  .holder-name {
    color: var(--brand-blue); font-weight: 700; font-size: 40px; line-height: 1.1;
  }
  .holder-title { color: var(--ink); font-size: 20px; font-weight: 400; margin-top: 2px; }
  .company-name {
    position: absolute; left: 110px; top: 205px;
    display: flex; align-items: center; gap: 14px;
    color: var(--brand-blue); font-weight: 700; font-size: 34px; line-height: 1.1;
  }
  .company-mark { width: 26px; height: 26px; background: var(--brand-blue); flex: none; }
  .contact {
    position: absolute; display: flex; align-items: center; gap: 10px;
    color: var(--on-blue); font-size: 21px; white-space: nowrap;
  }
  .contact svg { width: 20px; height: 20px; flex: none; }
  .contact-phone { left: 70px; top: 522px; }
  .contact-email { left: 370px; top: 478px; }
  .contact-web { right: 40px; top: 412px; }
</style>
</head>
<body>
  <article class="business-card">
    <svg class="wave-art" viewBox="0 0 1000 571" width="1000" height="571" aria-hidden="true">
      <path class="wave-line" d="M0 392 C200 452 430 476 630 370 C770 298 885 282 1000 278"
            fill="none" stroke="#8e8f91" stroke-width="12"/>
      <path class="wave-band" d="M0 425 C200 482 432 505 642 398 C782 326 890 310 1000 305 L1000 571 L0 571 Z"
            fill="#0a52a8"/>
    </svg>

    <div class="corner-tab"></div>

    <div class="holder">
      <p class="holder-name">Dana Whitfield</p>
      <p class="holder-title">Medical Manager</p>
    </div>

    <div class="company-name">
      <span class="company-mark"></span>
      <span>Northpeak Clinical Disposal</span>
    </div>

    <p class="contact contact-phone">
      <svg viewBox="0 0 24 24"><path fill="#fff" d="M6.6 10.8a15.1 15.1 0 0 0 6.6 6.6l2.2-2.2a1 1 0 0 1 1-.25 11.4 11.4 0 0 0 3.6.57 1 1 0 0 1 1 1V20a1 1 0 0 1-1 1A17 17 0 0 1 3 4a1 1 0 0 1 1-1h3.5a1 1 0 0 1 1 1c0 1.25.2 2.45.57 3.570a1 1 0 0 1-.25 1z"/></svg>
      555 014 7290
    </p>
    <p class="contact contact-email">
      <svg viewBox="0 0 24 24"><rect x="2" y="5" width="20" height="14" rx="1.5" fill="#fff"/><path d="M3 6.5l9 6.5 9-6.5" fill="none" stroke="#0a52a8" stroke-width="1.8"/></svg>
      info@northpeakclinical.com
    </p>
    <p class="contact contact-web">
      <svg viewBox="0 0 24 24"><circle cx="12" cy="12" r="10" fill="#fff"/><g fill="none" stroke="#0a52a8" stroke-width="1.4"><ellipse cx="12" cy="12" rx="4" ry="9"/><path d="M3 12h18M5 7h14M5 17h14"/></g></svg>
      www.northpeakclinical.com
    </p>
  </article>
</body>
</html>
```